Website redesign

We need a bold revamp of our website (http://www.brantocksparkworks.co.nz/)
which at the moment looks dated. We want a crisp, fresh and bold look. The background image behind web page can go. Open to complete new layout

Target Market(s)

Electrical contracting company- working in the domestic and commercial field

Coding

Coded - Design and coding required

Number of Pages Required

5+ page

Font styles to use
Sans Serif

Colors

Designer to choose colors to be used in the design.

```html
<!DOCTYPE html>
<html lang="en">
<head>
<meta charset="utf-8">
<title>Brantock Sparkworks</title>
<link rel="stylesheet" href="https://fonts.googleapis.com/css2?family=Lato:ital,wght@0,400;0,700;0,900;1,700&display=swap">
<style>
:root{
  --red:#e8141b;
  --red-dark:#c90f15;
  --black:#111111;
  --ink:#333333;
  --grey:#555555;
  --footer:#0d0d0d;
  --bar:#3a3a3a;
  --white:#ffffff;
}
*{box-sizing:border-box;margin:0;padding:0}
html,body{width:1200px;height:3822px;overflow:hidden;background:var(--white);font-family:'Lato',sans-serif;color:var(--ink)}
.page{position:relative;width:1200px;height:3822px}
.abs{position:absolute}

/* header */
.header{position:absolute;left:0;top:0;width:1200px;height:168px;background:var(--white)}
.callbar{position:absolute;left:655px;top:0;height:36px;width:335px;background:var(--black);border-radius:0 0 0 22px;display:flex;align-items:center;padding-left:22px;gap:8px;color:var(--white);font-size:14px;font-weight:700}
.callbar .label{color:var(--red)}
.callbar .dot{width:16px;height:16px;border-radius:50%;background:var(--red)}
.socials{position:absolute;left:1018px;top:9px;display:flex;gap:6px}
.socials span{width:22px;height:22px;border-radius:50%;background:var(--black)}
.brand{position:absolute;left:66px;top:48px;display:flex;align-items:center;gap:10px}
.brand .mark{width:28px;height:28px;background:var(--red)}
.brand .name{font-size:30px;font-weight:900;color:var(--black);line-height:1}
.nav{position:absolute;left:540px;top:76px;display:flex;align-items:center;font-size:15px;color:var(--black)}
.nav a{text-decoration:none;color:inherit;padding:4px 22px;border-right:1px solid #999;line-height:1}
.nav a:last-child{border-right:none}
.nav a.active{background:var(--red);color:var(--white);border-radius:14px;border-right:none;margin-right:8px;padding:7px 20px}
.badge{position:absolute;left:1100px;top:66px;width:60px;height:60px;border-radius:50%;background:#2f9e3a}

/* hero */
.hero{position:absolute;left:0;top:168px;width:1200px;height:492px;background:linear-gradient(110deg,#e6ebee 0%,#b8c4cc 35%,#5f7f91 60%,#d9dee0 100%)}
.arrow{position:absolute;width:40px;height:40px}
.arrow path{fill:none;stroke:var(--white);stroke-width:4}

/* about */
.about-photo{left:68px;top:735px;width:247px;height:670px;background:linear-gradient(180deg,#f1f1f1,#c7cfd6 60%,#8ea5b8)}
.section-title{display:flex;align-items:center;gap:12px;font-size:34px;font-weight:900;color:var(--black);letter-spacing:.5px}
.section-title .mark{width:42px;height:26px;background:var(--red)}
.about{left:428px;top:730px;width:710px}
.about .lead{margin-top:40px;color:var(--red);font-style:italic;font-weight:700;font-size:18px}
.about p{font-size:14.5px;line-height:1.55;color:var(--grey);margin-top:14px}
.about .lead+p{margin-top:14px}
.btn-dark{display:inline-block;margin-top:26px;width:138px;height:40px;background:var(--black);color:var(--white);font-size:11px;font-weight:700;text-align:center;line-height:40px}

/* services */
.services{position:absolute;left:0;top:1480px;width:1200px;height:970px;background:linear-gradient(180deg,#1d1d1d,#2a2a2a 50%,#161616)}
.centered-title{position:absolute;left:0;width:1200px;display:flex;flex-direction:column;align-items:center}
.centered-title .rule{width:46px;height:3px;margin-top:16px}
.services .section-title{color:var(--white)}
.services .rule{background:var(--white)}
.services .intro{position:absolute;left:270px;top:140px;width:660px;text-align:center;color:#e5e5e5;font-size:14px;line-height:1.55}
.services .intro p+p{margin-top:18px}
.btn-light{position:absolute;left:520px;top:295px;width:138px;height:40px;background:var(--white);color:var(--black);font-size:11px;font-weight:700;text-align:center;line-height:40px}
.tile{position:absolute;width:377px;height:86px;background:linear-gradient(135deg,#9fb3c2,#5e7384);overflow:hidden}
.tile .cap{position:absolute;left:0;bottom:0;width:100%;height:34px;background:rgba(0,0,0,.55);color:var(--white);font-size:25px;padding-left:6px;line-height:34px;letter-spacing:1px}

/* projects */
.projects-title{top:2498px}
.projects-title .rule{background:var(--black)}
.project{position:absolute;width:450px}
.project .thumb{position:absolute;left:0;width:125px;height:95px;background:linear-gradient(135deg,#c8d4de,#6f8799)}
.project .body{position:absolute;left:167px;width:330px}
.project h3{color:var(--red);font-size:14.5px;font-weight:700}
.project p{font-size:12.5px;line-height:1.55;color:var(--grey);margin-top:14px}
.project .more{font-size:12px;color:var(--black);margin-top:10px;display:block}
.project .more b{color:var(--red)}

/* testimonials */
.testimonials{position:absolute;left:0;top:3005px;width:1200px;height:445px;background:var(--red)}
.testimonials .section-title{color:var(--white);font-weight:400}
.testimonials .section-title .mark{background:var(--white);width:38px;height:24px}
.testimonials .rule{background:var(--white)}
.card{position:absolute;top:190px;width:310px;height:130px;border:1.5px solid var(--white);padding:18px 14px;color:var(--white)}
.card .q{position:absolute;left:14px;top:-14px;font-size:34px;font-weight:900;background:var(--red);padding:0 4px;line-height:30px}
.card h4{font-size:13px;font-weight:700}
.card p{font-size:12px;line-height:1.4;margin-top:6px}
.person{position:absolute;top:327px;display:flex;align-items:center;gap:10px;color:var(--white)}
.person .avatar{width:44px;height:44px;border-radius:50%;background:#f2f2f2;border:2px solid var(--white)}
.person b{font-size:12px;display:block}
.person span{font-size:11px;line-height:1.35;display:block}

/* footer */
.footer{position:absolute;left:0;top:3450px;width:1200px;height:310px;background:var(--footer);color:var(--white)}
.footer .brand{left:68px;top:60px}
.footer .brand .name{color:var(--white)}
.footer .about-text{position:absolute;left:68px;top:170px;width:200px;font-size:12.5px;line-height:1.4;color:#ddd}
.fcol{position:absolute;top:60px}
.fcol h5{font-size:16px;font-weight:700;color:var(--red);letter-spacing:1.5px}
.fcol .line{width:150px;height:1px;background:#555;margin:10px 0 14px}
.fcol ul{list-style:none;font-size:15px;line-height:1.75}
.fcol li::before{content:"› ";color:var(--red)}
.authorised{position:absolute;left:330px;top:60px;width:130px}
.authorised h5{color:var(--white);font-size:17px;line-height:1.25;letter-spacing:0}
.authorised .plate{width:115px;height:46px;background:var(--white);margin-top:10px}
.contact-list{font-size:13px;line-height:1.6;color:#ddd}
.contact-list .row{display:flex;align-items:center;gap:8px}
.contact-list .ic{width:11px;height:11px;background:var(--red);border-radius:50%}
.fsocial{display:flex;gap:7px}
.fsocial span{width:22px;height:22px;border-radius:50%;background:var(--white)}
.callus{margin-top:30px;font-size:17px;font-weight:700;line-height:1.25}
.bottombar{position:absolute;left:0;top:3760px;width:1200px;height:62px;background:var(--bar);color:#bbb;font-size:13px;text-align:center;line-height:62px}
</style>
</head>
<body>
<div class="page">

  <header class="header">
    <div class="callbar"><span class="dot"></span><span class="label">Call Us Free:</span> 0800 55 01 27 | (06)555 0143</div>
    <div class="socials"><span></span><span></span><span></span><span></span></div>
    <div class="brand"><span class="mark"></span><span class="name">Brantock<br><span style="font-size:17px;font-weight:400">SPARKWORKS</span></span></div>
    <nav class="nav">
      <a class="active" href="#">Home</a><a href="#">About us</a><a href="#">Services</a><a href="#">Projects</a><a href="#">Contact us</a>
    </nav>
    <div class="badge"></div>
  </header>

  <div class="hero" role="img" aria-label="Electrician working inside a switchboard full of coloured wiring"></div>
  <svg class="arrow" style="left:66px;top:392px" viewBox="0 0 40 40"><path d="M26 6 L12 20 L26 34"/></svg>
  <svg class="arrow" style="left:1092px;top:392px" viewBox="0 0 40 40"><path d="M14 6 L28 20 L14 34"/></svg>

  <div class="abs about-photo" role="img" aria-label="Electrician in white hard hat holding a cable"></div>
  <section class="abs about">
    <h2 class="section-title"><span class="mark"></span>ABOUT US</h2>
    <div class="lead">Proudly serving our local community for over 20 years</div>
    <p>Brantock Sparkworks is a leading electrical installation and maintenance company based in Tawhiti Bay, but servicing all New Zealand. We are proud to be locally owned and operated. With over 15 employees, we are a very professional qualified and experienced team of technicians and support staff.</p>
    <p>Brantock Sparkworks was established in 1991 and does it all, from supplying and changing light bulbs, comprehensive whole house electrical design and installation, to commercial and large scale industrial consultation, implementation and servicing.</p>
    <p>With over 20 years' experience in providing our customers with personalized service for their home electrical needs, individual lighting plans, experienced advise on renovations, heating and cooling requirements for home comfort, security systems and cameras, and providing the most up to date equipment and knowledge of energy efficiency and all electrical legislation.</p>
    <p>As Tawhiti Bay's top Norvane accredited installers and Tawhiti Bay's ONLY member of The Heat Pump Alliance of New Zealand (HPA) we aim to continue to provide the Tawhiti Bay region with the highest possible quality of professional service.</p>
    <p>Our goal is to provide you with the best possible electrical advice and service. In everything we do, from consultation and design to finishing the job, our commitment to providing reliable, high quality services is evident. Our electrical technicians are on call 24 hour, 7 days a week.</p>
    <p>Let us provide the peace of mind that comes with knowing that all workmanship is guaranteed and done to meet all the regulations and standards with integrity, experience and dedication.</p>
    <span class="btn-dark">READ MORE</span>
  </section>

  <section class="services">
    <div class="centered-title" style="top:68px"><h2 class="section-title"><span class="mark"></span>OUR SERVICES</h2><span class="rule"></span></div>
    <div class="intro">
      <p>Brantock Sparkworks offers all the domestic and commercial electrical services you would expect from an electrical firm, but with dedicated technicans in specialist electrical areas they have the more technical ability and experience than your average sparky.</p>
      <p>If you can't find what you are looking for in the appropriate sections listed, simply contact us on 0800 55 01 27 and we will be able to help you out.</p>
    </div>
    <span class="btn-light">READ MORE</span>
    <div class="tile" style="left:375px;top:367px" role="img" aria-label="Electrical cables and tools"><span class="cap">Electrical</span></div>
    <div class="tile" style="left:178px;top:477px" role="img" aria-label="Appliance testing equipment"><span class="cap">Appliance Testing</span></div>
    <div class="tile" style="left:578px;top:477px" role="img" aria-label="Alarm keypad"><span class="cap">Alarms</span></div>
    <div class="tile" style="left:178px;top:585px" role="img" aria-label="Security cameras on a wall"><span class="cap">Security Cameras</span></div>
    <div class="tile" style="left:578px;top:585px" role="img" aria-label="Heat pump unit"><span class="cap">Heat Pumps</span></div>
    <div class="tile" style="left:178px;top:693px" role="img" aria-label="Fire alarm call point"><span class="cap">Fire/Smoke</span></div>
    <div class="tile" style="left:578px;top:693px" role="img" aria-label="Building compliance inspection"><span class="cap">IQP Building Compliance</span></div>
    <div class="tile" style="left:178px;top:800px" role="img" aria-label="Network data cabling"><span class="cap">Phone/Data</span></div>
    <div class="tile" style="left:578px;top:800px" role="img" aria-label="Satellite dish and aerial"><span class="cap">TV - Satellite/Aerial</span></div>
  </section>

  <div class="centered-title projects-title"><h2 class="section-title"><span class="mark"></span>OUR PROJECTS</h2><span class="rule"></span></div>
  <div class="project" style="left:65px;top:2615px">
    <div class="thumb" style="top:0" role="img" aria-label="Commercial building interior installation"></div>
    <div class="body" style="top:-8px"><h3>Lorem ipsum dolor sit amet</h3><p>Lorem ipsum dolor sit amet, consectetur adipiscing elit. Quid autem habent admirationis,prope accessenis. Lorem ipsum dolor sit amet, consectetur adipiscing elit.</p><span class="more">Read more <b>»</b></span></div>
  </div>
  <div class="project" style="left:635px;top:2615px">
    <div class="thumb" style="top:0" role="img" aria-label="Blue network cabling in a rack"></div>
    <div class="body" style="top:-20px"><h3>Lorem ipsum dolor sit amet</h3><p>Lorem ipsum dolor sit amet, consectetur adipiscing elit. Quid autem habent admirationis,prope accessenis. Lorem ipsum dolor sit amet, consectetur adipiscing elit.</p><span class="more">Read more <b>»</b></span></div>
  </div>
  <div class="project" style="left:65px;top:2800px">
    <div class="thumb" style="top:0" role="img" aria-label="Switchboard wiring"></div>
    <div class="body" style="top:-8px"><h3>Lorem ipsum dolor sit amet</h3><p>Lorem ipsum dolor sit amet, consectetur adipiscing elit. Quid autem habent admirationis,prope accessenis. Lorem ipsum dolor sit amet, consectetur adipiscing elit.</p><span class="more">Read more <b>»</b></span></div>
  </div>
  <div class="project" style="left:635px;top:2800px">
    <div class="thumb" style="top:0" role="img" aria-label="Ceiling smoke detector"></div>
    <div class="body" style="top:-20px"><h3>Lorem ipsum dolor sit amet</h3><p>Lorem ipsum dolor sit amet, consectetur adipiscing elit. Quid autem habent admirationis,prope accessenis. Lorem ipsum dolor sit amet, consectetur adipiscing elit.</p><span class="more">Read more <b>»</b></span></div>
  </div>

  <section class="testimonials">
    <div class="centered-title" style="top:62px"><h2 class="section-title"><span class="mark"></span>Clients Testimonials</h2><span class="rule"></span></div>
    <svg class="arrow" style="left:66px;top:200px" viewBox="0 0 40 40"><path d="M26 6 L12 20 L26 34"/></svg>
    <svg class="arrow" style="left:1092px;top:200px" viewBox="0 0 40 40"><path d="M14 6 L28 20 L14 34"/></svg>
    <div class="card" style="left:258px"><span class="q">“</span><h4>Highly Professional Team</h4><p>Lorem ipsum dolor sit amet, consectetur adipiscing elit. Quid autem habent admirationis, cum prope accessenis? An hoc usque quaque, aliter in vita?</p></div>
    <div class="card" style="left:630px"><span class="q">“</span><h4>Highly Professional Team</h4><p>Lorem ipsum dolor sit amet, consectetur adipiscing elit. Quid autem habent admirationis, cum prope accessenis? An hoc usque quaque, aliter in vita?</p></div>
    <div class="person" style="left:275px"><span class="avatar" role="img" aria-label="Client portrait"></span><div><b>MR HALLOWAY</b><span>Sales manager at Corvell Freight<br>President at Tarnwick MP</span></div></div>
    <div class="person" style="left:647px"><span class="avatar" role="img" aria-label="Client portrait"></span><div><b>MR HALLOWAY</b><span>Sales manager at Corvell Freight<br>President at Tarnwick MP</span></div></div>
  </section>

  <footer class="footer">
    <div class="brand"><span class="mark"></span><span class="name">Brantock<br><span style="font-size:17px;font-weight:400">SPARKWORKS</span></span></div>
    <p class="about-text">Lorem ipsum dolor sit amet, consectetur adipiscing elit. Quid autem habent admirationis, cum prope accessens</p>
    <div class="fcol authorised"><h5>We are authorised installers for:</h5><div class="plate"></div><div class="plate"></div></div>
    <div class="fcol" style="left:520px"><h5>QUICK LINKS</h5><div class="line"></div><ul><li>Home</li><li>About us</li><li>Services</li><li>Projects</li><li>Contact us</li></ul></div>
    <div class="fcol" style="left:727px"><h5>CONTACT</h5><div class="line"></div>
      <div class="contact-list">
        <div>14 Kestrel Lane,<br>Tawhiti Bay 4599</div>
        <div class="row" style="margin-top:8px"><span class="ic"></span>0800 55 01 27</div>
        <div class="row"><span class="ic"></span>(06)555 0144</div>
        <div class="row"><span class="ic"></span>office@brantocksparkworks.co.nz</div>
        <div class="row"><span class="ic"></span>www.brantocksparkworks.co.nz</div>
      </div>
    </div>
    <div class="fcol" style="left:960px"><h5>FOLLOW US ON</h5><div class="line" style="width:170px"></div>
      <div class="fsocial"><span></span><span></span><span></span><span></span></div>
      <div class="callus">CALL US ON<br>0800 55 01 27<br>(06)555 0143</div>
    </div>
  </footer>
  <div class="bottombar">© 2018 Brantock Sparkworks | Privacy Policy | User Agreement</div>

</div>
</body>
</html>
```